Graphic Design for an online custom wine label company

Provides artistic and funky wine labels to people online. People can customize the text on the label.

```html
<!DOCTYPE html>
<html lang="en">
<head>
<meta charset="UTF-8">
<title>Wine Label – Name of Wine</title>
<link rel="stylesheet" href="https://fonts.googleapis.com/css2?family=Kaushan+Script&family=Roboto:ital,wght@0,300;0,400;0,700;1,400&display=swap">
<style>
  :root {
    --label-black: #000000;
    --accent-blue: #00aeef;
    --heart-red: #c1272d;
    --ink-white: #ffffff;
  }

  * { margin: 0; padding: 0; box-sizing: border-box; }

  html, body {
    width: 840px;
    height: 1200px;
    overflow: hidden;
    background: var(--label-black);
  }

  .label {
    position: relative;
    width: 840px;
    height: 1200px;
    background: var(--label-black);
    font-family: "Roboto", Arial, sans-serif;
    color: var(--ink-white);
  }

  .label__artwork {
    position: absolute;
    left: 270px;
    top: 62px;
    width: 300px;
    height: 562px;
    border-radius: 24px;
    background: radial-gradient(ellipse at 50% 45%,
      rgba(193, 39, 45, 0.85) 0%,
      rgba(193, 39, 45, 0.35) 30%,
      rgba(255, 255, 255, 0.12) 55%,
      rgba(0, 0, 0, 0) 75%);
  }

  .label__name {
    position: absolute;
    left: 0;
    top: 672px;
    width: 100%;
    text-align: center;
    font-family: "Kaushan Script", cursive;
    font-size: 76px;
    line-height: 1;
    color: var(--accent-blue);
  }

  .label__description {
    position: absolute;
    left: 60px;
    top: 814px;
    width: 720px;
    text-align: center;
    font-style: italic;
    font-weight: 400;
    font-size: 24.5px;
    line-height: 41px;
    color: var(--ink-white);
  }

  .label__band {
    position: absolute;
    left: 0;
    top: 960px;
    width: 840px;
    height: 240px;
    background: var(--accent-blue);
  }

  .label__vintage {
    position: absolute;
    left: 0;
    top: 26px;
    width: 100%;
    text-align: center;
    font-weight: 300;
    font-size: 46px;
    letter-spacing: 3px;
    line-height: 1.1;
  }

  .label__type {
    position: absolute;
    left: 0;
    top: 86px;
    width: 100%;
    text-align: center;
    font-weight: 700;
    font-size: 34px;
    letter-spacing: 1.5px;
    line-height: 1.1;
  }

  .label__volume,
  .label__origin {
    position: absolute;
    top: 176px;
    font-weight: 400;
    font-size: 29px;
    line-height: 1.1;
  }

  .label__volume { left: 72px; }
  .label__origin { right: 73px; }
</style>
</head>
<body>
  <main class="label">
    <div class="label__artwork" role="img" aria-label="Hand-drawn white wine glass with a red heart inside and two red hearts floating above it"></div>

    <h1 class="label__name">Name of Wine</h1>

    <p class="label__description">
      Idunt luptat, venim nim volortie veriust ionsecte tate<br>
      magna feugait, quiscipit vel eugue tat, velendignim<br>
      nero tilicit illarissulus conte nime receps, Eperfenem
    </p>

    <section class="label__band">
      <p class="label__vintage">SELECTION 2012</p>
      <p class="label__type">TYPE OF WINE</p>
      <p class="label__volume">XXX ml</p>
      <p class="label__origin">PRODUCT OF CITY</p>
    </section>
  </main>
</body>
</html>
```